依頼詳細
(例)毎年忘年会・新年会チラシをうちます。その広告デザインをお願い致します。今年は新企画として女子会プランを紙面の半分のスペースに入れたいと思います。明るく楽しく見やすい和のデザインをお願いします。
記載項目
(例)入る原稿(文字、写真)はイラストレーターCS2にて添付します。裏面は昨年から流用しますので表面には住所や地図は入りません。タイトルをいじったりキャッチコピーを入れて下さってかまいません。
希望イメージ
シンプル 複雑
単色 カラフル
暗い 明るい
日常 高級
遊び心 厳粛
未来的 伝統的
女性的 男性的
希望する色
(例)赤、黒(特にこだわりません)
納品ファイル
• 高解像度JPG (.jpg)
• イラストレーター形式 (.ai)
補足説明
■ 選んだ理由

明るく楽しげな雰囲気がとてもよかったです。女子会のタイトルの工夫もいい感じです。

■ 提案者全員のお礼・コメント

多くの方に提案して頂きありがとうございました。1つ選ぶのは心苦しいのですが選んだ納得感が気に入っています。またお願いするときにはよろしくお願いします。

```html
<!DOCTYPE html>
<html lang="ja">
<head>
<meta charset="utf-8">
<title>福鮨 忘年会・新年会 / 女子会セット</title>
<link href="https://fonts.googleapis.com/css2?family=Shippori+Mincho:wght@500;800&family=Yuji+Syuku&family=Noto+Sans+JP:wght@400;700;900&display=swap" rel="stylesheet">
<style>
:root{
  --red:#c8102e;
  --red-deep:#8e1422;
  --wine:#5b1a20;
  --ink:#161616;
  --gold:#d9b15a;
  --white:#ffffff;
  --cream:#f6ebe0;
  --blush:#ecd0cc;
  --bar:#f3efe9;
}
*{margin:0;padding:0;box-sizing:border-box}
html,body{width:849px;height:1200px;overflow:hidden;background:var(--white)}
.flyer{position:relative;width:849px;height:1200px;overflow:hidden;
  background:linear-gradient(180deg,var(--red-deep) 0,var(--wine) 700px,var(--cream) 700px,var(--blush) 1200px);
  font-family:"Noto Sans JP",sans-serif;color:var(--ink)}
.abs{position:absolute}

/* title block */
.title-block{left:26px;top:26px;width:358px;height:310px;background:var(--ink);border:3px solid var(--gold);
  display:flex;flex-direction:column;align-items:center;justify-content:center;gap:8px}
.brand{display:flex;align-items:center;gap:10px;color:var(--white);font-family:"Shippori Mincho",serif;font-weight:800;font-size:44px}
.brand-dot{width:26px;height:26px;border-radius:50%;background:var(--red)}
.title{font-family:"Yuji Syuku",serif;color:var(--white);font-size:84px;line-height:1.05;text-align:center;font-weight:400}

/* plans */
.plan-head{left:396px;top:22px;width:426px;height:50px;display:flex;align-items:center;justify-content:space-between;color:var(--white)}
.plan-head small{font-size:13px;line-height:1.3}
.plan-head .price{background:var(--red);color:var(--white);padding:2px 12px;font-family:"Shippori Mincho",serif;font-weight:800;font-size:34px;white-space:nowrap}
.plan-head .price span{font-size:16px}
.plan{left:396px;width:426px;height:60px;background:var(--bar);display:flex;align-items:center;gap:14px;border-left:6px solid var(--gold)}
.plan-mark{width:60px;height:60px;flex:none;background:var(--wine);color:var(--white);font-family:"Yuji Syuku",serif;font-size:38px;display:flex;align-items:center;justify-content:center}
.plan-body{display:flex;flex-direction:column}
.plan-price{font-family:"Shippori Mincho",serif;font-weight:800;font-size:28px;color:var(--red-deep);line-height:1}
.plan-price span{font-size:14px;color:var(--ink)}
.plan-menu{font-size:11px;color:#444;margin-top:3px;white-space:nowrap}

/* middle offers */
.offer{background:var(--white);border:3px solid var(--gold)}
.offer-tag{position:absolute;left:0;top:0;right:0;height:40px;background:var(--ink);color:var(--white);display:flex;align-items:center;justify-content:space-between;padding:0 10px;font-weight:700;font-size:16px;white-space:nowrap}
.offer-tag b{font-family:"Shippori Mincho",serif;font-size:30px;color:var(--gold)}
.offer-tag b small{font-size:14px}
.photo{position:absolute;border-radius:2px}
.tag-req{background:var(--red);color:var(--white);font-size:12px;padding:2px 6px}
.drink{left:426px;top:390px;width:396px;height:180px}
.drink-body{position:absolute;left:0;right:0;top:40px;bottom:0;display:flex;align-items:center;justify-content:center;gap:18px;background:var(--cream)}
.circle{width:84px;height:84px;border-radius:50%;background:var(--red);color:var(--white);display:flex;flex-direction:column;align-items:center;justify-content:center;font-weight:700;font-size:13px;line-height:1.2}
.circle b{font-size:30px}
.drink-text{font-family:"Shippori Mincho",serif;font-weight:800;font-size:32px;color:var(--red-deep);white-space:nowrap}

.discount{left:26px;top:596px;width:372px;height:92px;display:flex;align-items:center;gap:14px;padding:0 14px}
.pct{background:var(--red);color:var(--white);font-family:"Shippori Mincho",serif;font-weight:800;font-size:40px;padding:4px 10px;line-height:1;text-align:center}
.pct span{font-size:20px}
.discount p{font-weight:700;font-size:20px;line-height:1.35}
.bus{left:426px;top:596px;width:396px;height:92px;display:flex;align-items:center;gap:14px;padding:0 14px}
.bus p{font-weight:900;font-size:22px;color:var(--red-deep);line-height:1.3}
.bus small{display:block;font-weight:400;font-size:11px;color:#444}

/* girls' set */
.set-brand{left:26px;top:722px;width:130px;height:128px;background:var(--ink);color:var(--white);
  display:flex;flex-direction:column;align-items:center;justify-content:center;font-family:"Shippori Mincho",serif;font-weight:800;font-size:34px;line-height:1.2}
.set-brand span{font-size:20px}
.set-title{left:180px;top:716px;width:643px;height:140px;font-family:"Yuji Syuku",serif;font-weight:400;color:var(--red);font-size:108px;line-height:140px;text-align:center;white-space:nowrap;letter-spacing:2px}
.set-title .set-word{font-size:72px;letter-spacing:0}
.course{width:380px;top:1058px;height:100px;display:flex;align-items:center;justify-content:space-between}
.course-name{background:var(--red);color:var(--white);font-family:"Shippori Mincho",serif;font-weight:800;font-size:22px;line-height:1.25;padding:8px 12px}
.course-price{font-family:"Shippori Mincho",serif;font-weight:800;font-size:44px;color:var(--ink);white-space:nowrap}
.course-price span{font-size:24px}
</style>
</head>
<body>
<main class="flyer">

  <section class="abs title-block">
    <div class="brand"><span class="brand-dot"></span>福鮨</div>
    <h1 class="title">忘年会<br>新年会</h1>
  </section>

  <header class="abs plan-head">
    <small>お料理とお飲み物<br>全品飲み放題付</small>
    <div class="price">3,500<span>円より</span></div>
  </header>

  <div class="abs plan" style="top:86px">
    <div class="plan-mark">彩</div>
    <div class="plan-body"><div class="plan-price">3,500<span>円（税込）</span></div><div class="plan-menu">前菜・造り盛合せ・焼物・揚物・食事・デザート</div></div>
  </div>
  <div class="abs plan" style="top:162px">
    <div class="plan-mark">雅</div>
    <div class="plan-body"><div class="plan-price">4,000<span>円（税込）</span></div><div class="plan-menu">前菜・造り盛合せ・煮物・揚物・上寿司・デザート</div></div>
  </div>
  <div class="abs plan" style="top:238px">
    <div class="plan-mark">曙</div>
    <div class="plan-body"><div class="plan-price">5,000<span>円（税込）</span></div><div class="plan-menu">前菜・特選造り・焼物・鍋物・上寿司・フルーツ</div></div>
  </div>
  <div class="abs plan" style="top:314px">
    <div class="plan-mark">艶</div>
    <div class="plan-body"><div class="plan-price">7,000<span>円（税込）</span></div><div class="plan-menu">先付・特選造り・蟹料理・鍋物・特上寿司・フルーツ</div></div>
  </div>

  <section class="abs offer" style="left:26px;top:390px;width:372px;height:190px">
    <div class="offer-tag">寄せ鍋コース <b>3,500<small>円より</small></b> <span class="tag-req">要予約</span></div>
    <div class="photo" role="img" aria-label="寄せ鍋コースの料理写真" style="left:8px;top:48px;right:8px;bottom:8px;background:linear-gradient(135deg,#6b3a22,#c9803f 55%,#e7c38a)"></div>
  </section>

  <section class="abs offer drink">
    <div class="offer-tag">お得な宴会プラン <b>5,000<small>円</small></b> <span class="tag-req">要予約</span></div>
    <div class="drink-body">
      <div class="circle">飲み放題<b>2</b>時間</div>
      <div class="drink-text">お料理＋お飲物</div>
    </div>
  </section>

  <section class="abs offer discount">
    <div class="pct">5<span>%</span><br><span>OFF</span></div>
    <p>お食事券にて<br>お返し致します。</p>
  </section>

  <section class="abs offer bus">
    <svg width="110" height="56" viewBox="0 0 110 56" aria-hidden="true">
      <rect x="2" y="4" width="104" height="40" rx="6" fill="#f3efe9" stroke="#161616" stroke-width="3"/>
      <rect x="10" y="11" width="18" height="14" fill="#8fb7d6"/><rect x="32" y="11" width="18" height="14" fill="#8fb7d6"/>
      <rect x="54" y="11" width="18" height="14" fill="#8fb7d6"/><rect x="78" y="11" width="22" height="22" fill="#8fb7d6"/>
      <circle cx="24" cy="46" r="7" fill="#161616"/><circle cx="84" cy="46" r="7" fill="#161616"/>
    </svg>
    <p>送迎バス<br>ご利用ください<small>15名様以上でご利用いただけます</small></p>
  </section>

  <section class="abs set-brand">福鮨<span>オリジナル</span></section>
  <h2 class="abs set-title">女子会<span class="set-word">セット</span></h2>

  <div class="abs photo" role="img" aria-label="女子会上寿司コースの寿司とデザートの写真" style="left:26px;top:866px;width:380px;height:184px;background:linear-gradient(135deg,#2a2a2a,#b8584a 50%,#f2e2d2)"></div>
  <div class="abs photo" role="img" aria-label="女子会御膳コースの御膳料理の写真" style="left:440px;top:866px;width:380px;height:184px;background:linear-gradient(135deg,#4a1c1c,#c4463a 50%,#f0d7b8)"></div>

  <div class="abs course" style="left:26px">
    <div class="course-name">女子会<br>上寿司コース</div>
    <div class="course-price">2,500<span>yen</span></div>
  </div>
  <div class="abs course" style="left:440px">
    <div class="course-name">女子会<br>御膳コース</div>
    <div class="course-price">2,500<span>yen</span></div>
  </div>

</main>
</body>
</html>
```